Visitenkarten-Design für Rohrreinigungsfirma
Zielgruppe
Wir sind eine Kanal.-Rohrreinigungsfirma und suchen ein hochwertiges Design, unsere Zielgruppe sind Firmenkunden,Hausverwaltungen, Architekten sowie Behörden.
Aufgabenstellung
Das Design sollte Edel aussehen. Es sollten unsere Dienstleistungen mit auf der Visitenkarte stehen (gerne auch Rückseite): grabenlose Kanalsanierung, TV-Kamerainspektion,Dichtheitsprüfung DIN EN 1610, Fräsarbeiten mit Roboter, Fräsarbeiten mit Wasserhöchstdruck 2.500 Bar,Verstopfungsbeseitigung. (Vorderseite sollte enthalten:

```html
<!DOCTYPE html>
<html lang="de">
<head>
<meta charset="utf-8">
<title>Kalbern Visitenkarte</title>
<link rel="stylesheet" href="https://fonts.googleapis.com/css2?family=Fira+Sans:wght@400;500;600&family=Montserrat:wght@700;800&display=swap">
<style>
  :root {
    --backdrop: #b9b5b2;
    --paper: #ffffff;
    --brand-blue: #3b5f8a;
    --card-blue: #3d6088;
    --ink: #3a3e46;
    --ink-soft: #2f333a;
    --list-text: #e7edf4;
    --alert-red: #c93a40;
    --white: #ffffff;
  }
  html, body {
    margin: 0;
    padding: 0;
    width: 1200px;
    height: 910px;
    overflow: hidden;
    background: var(--backdrop);
  }
  .stage {
    position: relative;
    width: 1200px;
    height: 910px;
  }
  .card {
    position: absolute;
    left: 329px;
    width: 543px;
    height: 329px;
    box-sizing: border-box;
  }
  .card--front {
    top: 81px;
    background: var(--paper);
  }
  .card--back {
    top: 476px;
    height: 330px;
    background: var(--card-blue);
  }

  /* Front */
  .brand {
    position: absolute;
    left: 43px;
    top: 30px;
    display: flex;
    align-items: center;
    gap: 16px;
  }
  .brand__name {
    font-family: "Montserrat", sans-serif;
    font-weight: 800;
    font-size: 72px;
    line-height: 1;
    letter-spacing: -2px;
    color: var(--brand-blue);
  }
  .brand__dot {
    width: 54px;
    height: 54px;
    border-radius: 50%;
    background: var(--brand-blue);
  }
  .tagline {
    position: absolute;
    left: 43px;
    top: 126px;
    margin: 0;
    font-family: "Montserrat", sans-serif;
    font-weight: 700;
    font-size: 29px;
    letter-spacing: 0.2px;
    color: var(--ink);
  }
  .contact {
    position: absolute;
    top: 222px;
    margin: 0;
    font-family: "Fira Sans", sans-serif;
    font-size: 15.5px;
    line-height: 23.3px;
    color: var(--ink-soft);
    font-style: normal;
  }
  .contact--company { left: 43px; }
  .contact--reach { left: 304px; }
  .contact__firm { font-weight: 600; letter-spacing: 0.2px; }
  .contact__label { display: inline-block; width: 22px; }

  /* Back */
  .services {
    position: absolute;
    left: 50px;
    top: 28px;
    margin: 0;
    padding: 0;
    list-style: none;
    font-family: "Fira Sans", sans-serif;
    font-weight: 500;
    font-size: 17.5px;
    color: var(--list-text);
    letter-spacing: 0.2px;
  }
  .services__item {
    display: flex;
    align-items: center;
    height: 34px;
  }
  .services__tick {
    width: 15px;
    height: 12px;
    margin-right: 14px;
    flex: none;
  }
  .emergency {
    position: absolute;
    left: 46px;
    top: 248px;
    width: 450px;
    height: 54px;
    border-radius: 10px;
    background: var(--alert-red);
    display: flex;
    align-items: center;
    font-family: "Fira Sans", sans-serif;
    font-size: 24px;
    color: var(--white);
  }
  .emergency__icon {
    width: 32px;
    height: 32px;
    margin: 0 26px 0 24px;
  }
</style>
</head>
<body>
<main class="stage">
  <section class="card card--front" aria-label="Vorderseite">
    <div class="brand">
      <span class="brand__name">Kalbern</span>
      <span class="brand__dot" aria-hidden="true"></span>
    </div>
    <h1 class="tagline">KANAL- &amp; ROHRREINIGUNG</h1>
    <address class="contact contact--company">
      <span class="contact__firm">KALBERN KANAL.-ROHRREINIGUNG</span><br>
      Lindenweg 14<br>
      73450 Ahlbach/Steinfeld<br>
      Geschäftsführer: Jonas Reuter
    </address>
    <address class="contact contact--reach">
      <span class="contact__label">T</span>07342/581 27 19<br>
      <span class="contact__label">M</span>0160/300 700 45<br>
      info@rohrreinigung-kalbern.de<br>
      www.rohrreinigung-kalbern.de
    </address>
  </section>

  <section class="card card--back" aria-label="Rückseite">
    <ul class="services">
      <li class="services__item"><svg class="services__tick" viewBox="0 0 15 12"><path d="M1 6.5 L5 10.5 L14 1" fill="none" stroke="var(--list-text)" stroke-width="1.8"/></svg>grabenlose Kanalsanierung</li>
      <li class="services__item"><svg class="services__tick" viewBox="0 0 15 12"><path d="M1 6.5 L5 10.5 L14 1" fill="none" stroke="var(--list-text)" stroke-width="1.8"/></svg>TV-Kamerainspektion</li>
      <li class="services__item"><svg class="services__tick" viewBox="0 0 15 12"><path d="M1 6.5 L5 10.5 L14 1" fill="none" stroke="var(--list-text)" stroke-width="1.8"/></svg>Dichtheitsprüfung DIN EN 1610</li>
      <li class="services__item"><svg class="services__tick" viewBox="0 0 15 12"><path d="M1 6.5 L5 10.5 L14 1" fill="none" stroke="var(--list-text)" stroke-width="1.8"/></svg>Fräsarbeiten mit Roboter</li>
      <li class="services__item"><svg class="services__tick" viewBox="0 0 15 12"><path d="M1 6.5 L5 10.5 L14 1" fill="none" stroke="var(--list-text)" stroke-width="1.8"/></svg>Fräsarbeiten mit Wasserhöchstdruck 2.500 Bar</li>
      <li class="services__item"><svg class="services__tick" viewBox="0 0 15 12"><path d="M1 6.5 L5 10.5 L14 1" fill="none" stroke="var(--list-text)" stroke-width="1.8"/></svg>Verstopfungsbeseitigung</li>
    </ul>
    <div class="emergency">
      <svg class="emergency__icon" viewBox="0 0 32 32" aria-hidden="true">
        <circle cx="16" cy="16" r="14" fill="none" stroke="var(--white)" stroke-width="2.4"/>
        <path d="M16 8 V17 H10" fill="none" stroke="var(--white)" stroke-width="2.4"/>
      </svg>
      24h Notdienst Tag &amp; Nacht
    </div>
  </section>
</main>
</body>
</html>
```